Business Card Design job - Tessa's Business Cards

Simple elegant feminine design - Going out on my own as a Mortgage Broker.
My thoughts are the following details on the Front, middle of the card possibly? Phone and email smaller font than my name?
Tessa Marwick
Finance Specialist
p: 0438 217 905
e: tessa@marwickfinance.com.au
Bottom of the card
residential / commercial / equipment
I would like the Font in Rose Gold maybe white or black background? or Possibly a stone grey - are you able to do a few options? I'd like them embossed
Then I had an idea as a simple logo as per the attached if you get the idea in my scribble, my initials, capital T attached to a small m that leads/follows into a circle? Thicker Font In Rose Gold, middle of the card at the back.
Very open to ideas though and what colour you think would look better with the Rose Gold.
Thanks so much for your help, I am not very creative and savvy with this stuff :-)
Industry/Entity Type
Finance
Contact Information for Business Card
Tessa Marwick
p: 0438 217 905
Look and feel
Each slider illustrates characteristics of the customer's brand and the style your logo design should communicate.

```html
<!DOCTYPE html>
<html lang="en">
<head>
<meta charset="utf-8">
<title>Marwick Finance – Business Cards</title>
<link rel="stylesheet" href="https://fonts.googleapis.com/css2?family=Montserrat:wght@400;500;600&display=swap">
<style>
  :root {
    --backdrop: #8b8b8d;
    --card-black: #1e1e1f;
    --card-stone: #858aa0;
    --rose-light: #f4c6d6;
    --rose-mid: #e7879f;
    --rose-deep: #c9577a;
    --white: #f2f2f2;
  }
  * { margin: 0; padding: 0; box-sizing: border-box; }
  html, body {
    width: 1023px;
    height: 1200px;
    overflow: hidden;
    background: var(--backdrop);
    font-family: "Montserrat", sans-serif;
  }
  .sheet {
    position: relative;
    width: 1023px;
    height: 1200px;
  }
  .card {
    position: absolute;
    left: 131px;
    width: 760px;
    height: 434px;
    display: flex;
    flex-direction: column;
    align-items: center;
    box-shadow: 0 6px 18px rgba(0,0,0,0.22);
  }
  .card--brand {
    top: 120px;
    background: var(--card-black);
  }
  .card--contact {
    top: 640px;
    background: var(--card-stone);
    justify-content: center;
  }
  .rose-foil {
    background: linear-gradient(100deg, var(--rose-deep) 0%, var(--rose-mid) 35%, var(--rose-light) 55%, var(--rose-mid) 75%, var(--rose-deep) 100%);
    -webkit-background-clip: text;
    background-clip: text;
    color: transparent;
  }
  .brand-name {
    margin-top: 190px;
    font-size: 25px;
    font-weight: 600;
    letter-spacing: 0.32em;
    text-transform: uppercase;
  }
  .services {
    position: absolute;
    bottom: 56px;
    color: var(--white);
    font-size: 15px;
    font-weight: 400;
    letter-spacing: 0.02em;
    display: flex;
    gap: 12px;
    align-items: center;
  }
  .services .dot {
    width: 5px;
    height: 5px;
    border-radius: 50%;
    background: var(--white);
  }
  .holder-name {
    font-size: 27px;
    font-weight: 600;
    letter-spacing: 0.32em;
    text-transform: uppercase;
  }
  .holder-title {
    margin-top: 4px;
    font-size: 14px;
    font-weight: 600;
    letter-spacing: 0.34em;
    text-transform: uppercase;
  }
  .divider {
    width: 18px;
    height: 2px;
    margin: 10px 0 9px;
    background: var(--rose-mid);
  }
  .contact-line {
    font-size: 15px;
    font-weight: 400;
    letter-spacing: 0.1em;
    color: var(--rose-mid);
    line-height: 1.55;
  }
</style>
</head>
<body>
  <main class="sheet">
    <section class="card card--brand">
      <h1 class="brand-name rose-foil">Marwick Finance</h1>
      <p class="services">
        <span>Residential</span><span class="dot"></span>
        <span>Commercial</span><span class="dot"></span>
        <span>Equipment</span>
      </p>
    </section>

    <section class="card card--contact">
      <h2 class="holder-name rose-foil">Tessa Marwick</h2>
      <p class="holder-title rose-foil">Finance Specialist</p>
      <span class="divider"></span>
      <p class="contact-line">P: 0438 217 905</p>
      <p class="contact-line">e: tessa@marwickfinance.com.au</p>
    </section>
  </main>
</body>
</html>
```